The Nine Gates for Tablet Reliance - Contemporary Book Cover Design

The Nine Gates for Tablet Reliance was published in March 2019 and is available on Brimora and other platforms now. However, I am not happy with the cover.  It's a good design in some ways - I thought it would stand out and be easily recognizable. But I don't really like the color scheme and feel that a self-help book should probably use some lighter colors and that the red is too strident. The color scheme carries over into other marketing materials like the website, social media, etc. and I don't like the red and black scheme for these purposes.
It's not essential that the cover contain an endorsement like the current one but it could. Here are some endorsements:
“A must-read for anyone who is addicted to or thinks they may have a problem with digital technology. This eloquent work will also be useful to academics and clinicians exploring potential solutions. The author recognizes the similarities between smartphone addiction and other addictions, and logically applies one of the most effective known solutions for addiction - The Nine Gates.”
-- Dale Wickersham: Noted Interventionist, Keynote Speaker and Addiction Visionary
“If you suffer from digital addiction, I strongly encourage you to use this book as your road map to get you back to the real world.”
-- Thomas Quillard, Founder of Online Channel Monitor.
The back cover would have the new design / color scheme, but can have similar text, bio, author image, etc. Or we could include the endorsements there and shorten the other text.
As for the cover it could be stylized, or an image, a partial image, or whatever. I am open to suggestions. Think about what would be inviting for a person searching for help with moderating their smartphone use.
Let's add a subtitle as well "An Inner Journey to Balanced Tablet Habits"
Here is a link to the book:
https://www.brimora.example/Nine-Gates-Tablet-Reliance/dp/4086213590

Target Market(s)
General, since this issue affects almost everyone.
Colors
Designer to choose colors to be used in the design.
Look and feel

```html
<!DOCTYPE html>
<html lang="en">
<head>
<meta charset="utf-8">
<title>The Nine Gates for Tablet Reliance – Cover</title>
<link rel="stylesheet" href="https://fonts.googleapis.com/css2?family=Russo+One&family=Teko:wght@500;600&display=swap">
<style>
  :root {
    --backdrop: #dfe6ea;
    --cover-light: #fbf8f2;
    --cover-mid: #f1ece2;
    --cover-edge: #e3ddd1;
    --ink: #46556a;
    --ink-soft: #5a6a7e;
    --accent: #4f9a93;
    --accent-deep: #3f867f;
    --rule: #cfc8ba;
    --art-light: #dcebe8;
    --art-mid: #b9d3cf;
    --art-dark: #8fb2ad;
  }
  html, body {
    margin: 0;
    padding: 0;
    width: 1200px;
    height: 1200px;
    overflow: hidden;
    background: var(--backdrop);
  }
  .cover {
    position: absolute;
    left: 260px;
    top: 40px;
    width: 680px;
    height: 1120px;
    background: radial-gradient(ellipse at 50% 40%, var(--cover-light) 0%, var(--cover-mid) 70%, var(--cover-edge) 100%);
    overflow: hidden;
  }
  .cover__subtitle,
  .cover__title-lead,
  .cover__title-key,
  .cover__title-end,
  .cover__author {
    position: absolute;
    left: 0;
    width: 100%;
    margin: 0;
    text-align: center;
    text-transform: uppercase;
    white-space: nowrap;
  }
  .cover__subtitle {
    top: 56px;
    font-family: "Teko", sans-serif;
    font-weight: 600;
    font-size: 30px;
    line-height: 34px;
    letter-spacing: 1.5px;
    color: var(--ink);
  }
  .cover__title {
    margin: 0;
    font-family: "Russo One", sans-serif;
    font-weight: 400;
  }
  .cover__title-lead {
    top: 128px;
    font-size: 52px;
    line-height: 58px;
    letter-spacing: 4px;
    color: var(--ink-soft);
  }
  .cover__title-key {
    top: 205px;
    font-size: 80px;
    line-height: 84px;
    letter-spacing: 3px;
    color: var(--accent);
    transform: skewX(-10deg);
  }
  .cover__title-end {
    top: 304px;
    font-size: 92px;
    line-height: 96px;
    letter-spacing: 2px;
    color: var(--accent-deep);
  }
  .cover__art {
    position: absolute;
    left: 239px;
    top: 464px;
    width: 222px;
    height: 504px;
    border-radius: 34px;
    background: linear-gradient(180deg, var(--art-light) 0%, var(--art-mid) 55%, var(--art-dark) 100%);
  }
  .cover__floor-rule {
    position: absolute;
    left: 0;
    top: 885px;
    width: 100%;
    height: 2px;
    background: var(--rule);
    transform: rotate(-0.6deg);
  }
  .cover__author {
    top: 1030px;
    font-family: "Russo One", sans-serif;
    font-size: 34px;
    line-height: 40px;
    letter-spacing: 6px;
    color: var(--ink);
  }
</style>
</head>
<body>
  <main class="cover">
    <p class="cover__subtitle">An Inner Journey to Balanced Tablet Habits</p>
    <h1 class="cover__title">
      <span class="cover__title-lead">The 9 Gates for</span>
      <span class="cover__title-key">Tablet</span>
      <span class="cover__title-end">Reliance</span>
    </h1>
    <div class="cover__floor-rule"></div>
    <div class="cover__art" role="img" aria-label="Illustration of a tablet screen showing a figure standing behind bars, casting a shadow"></div>
    <p class="cover__author">Martin Halvey</p>
  </main>
</body>
</html>
```